Business card design for Automotive workshop

We need a business card for a new automotive repair and tyre shop called Ridgeback Prime Automotive located in New Zealand. We are a clean, modern and fresh workshop and company.

Front needs to feature logo,
my name:
Lachie Westergaard (director)

Address:
48 Marlow Lane
Kereru Bay 3592

Phone: 07 842 1937
Mobile: 027 519 2764
Email: office@ridgebackmotors.co.nz
Website: ridgebackmotors.co.nz

Back needs to feature an area to write down appointment details, date and time.

Also feature a list of jobs and work we do such as,
Vehicle Servicing
All Mechanical Repairs
Warrant of Fitness
Tyres & Wheel Alignments
Automotive Diagnostics
Automotive Parts & Supplies

```html
<!DOCTYPE html>
<html lang="en">
<head>
<meta charset="utf-8">
<title>Ridgeback Prime Automotive – Business Card</title>
<link rel="stylesheet" href="https://fonts.googleapis.com/css2?family=Ubuntu:wght@500;700&family=Open+Sans:wght@400&display=swap">
<style>
  :root {
    --backdrop: #cdbcbc;
    --card-dark: #000000;
    --card-light: #f7f7f7;
    --brand-red: #c41e27;
    --ink-white: #ffffff;
    --ink-dark: #1c1c1c;
  }
  * { box-sizing: border-box; margin: 0; padding: 0; }
  html, body { width: 1200px; height: 1200px; overflow: hidden; }
  body { background: var(--backdrop); position: relative; font-family: "Open Sans", sans-serif; }

  .card { position: absolute; left: 250px; width: 700px; height: 400px; overflow: hidden; }
  .card--front { top: 147px; background: var(--card-dark); }
  .card--back { top: 652px; background: linear-gradient(135deg, #ffffff 0%, var(--card-light) 55%, #e9e9e9 100%); }

  .brand-name {
    position: absolute; left: 0; width: 100%; text-align: center;
    font-family: "Ubuntu", sans-serif; font-weight: 700; font-size: 31px;
    letter-spacing: 1px; text-transform: uppercase; color: var(--brand-red);
  }
  .card--front .brand-name { top: 72px; }
  .card--back .brand-name { top: 40px; }

  .identity { position: absolute; right: 395px; top: 214px; text-align: right; font-family: "Ubuntu", sans-serif; }
  .identity__name { font-size: 27px; font-weight: 700; color: var(--brand-red); line-height: 1.2; }
  .identity__role { font-size: 21px; font-weight: 700; color: var(--ink-white); margin-top: 4px; }
  .identity__address { font-size: 21px; font-weight: 700; color: var(--ink-white); margin-top: 26px; line-height: 1.35; }

  .divider { position: absolute; left: 331px; top: 208px; width: 2px; height: 165px; background: var(--ink-white); }

  .contacts { position: absolute; left: 348px; top: 218px; list-style: none; }
  .contact { display: flex; align-items: center; color: var(--ink-white); height: 30px; }
  .contact + .contact { margin-top: 11px; }
  .contact--web { margin-top: 6px !important; }
  .contact__icon { width: 24px; height: 24px; margin-right: 11px; flex: none; }
  .contact__text { font-size: 21px; }
  .contact__text--small { font-size: 18px; }

  .appointment { position: absolute; left: 38px; top: 136px; width: 602px; color: var(--ink-dark); }
  .appointment__title { font-size: 30px; font-weight: 400; }
  .field { display: flex; align-items: baseline; font-size: 24px; margin-top: 22px; }
  .field:first-of-type { margin-top: 24px; }
  .field__line { flex: 1; margin-left: 8px; border-bottom: 2px dotted var(--ink-dark); transform: translateY(-5px); }

  .services {
    position: absolute; left: 0; bottom: 0; width: 100%; height: 89px; background: var(--card-dark);
    display: flex; justify-content: space-around; align-items: center; padding: 0 12px;
  }
  .services__group { list-style: none; text-align: center; font-family: "Ubuntu", sans-serif; font-weight: 700; font-size: 16.5px; color: var(--brand-red); line-height: 1.3; }
</style>
</head>
<body>

<section class="card card--front" aria-label="Business card front">
  <div class="brand-name">Ridgeback Prime Automotive</div>

  <div class="identity">
    <p class="identity__name">Lachie Westergaard</p>
    <p class="identity__role">director</p>
    <p class="identity__address">48 Marlow Lane<br>Kereru Bay 3592</p>
  </div>

  <div class="divider"></div>

  <ul class="contacts">
    <li class="contact">
      <svg class="contact__icon" viewBox="0 0 24 24" aria-hidden="true"><path fill="#c41e27" d="M6.6 10.8a15.1 15.1 0 0 0 6.6 6.6l2.2-2.2c.3-.3.7-.4 1-.2 1.1.4 2.3.6 3.6.6.6 0 1 .4 1 1V20c0 .6-.4 1-1 1A17 17 0 0 1 3 4c0-.6.4-1 1-1h3.5c.6 0 1 .4 1 1 0 1.3.2 2.5.6 3.6.1.3 0 .7-.2 1z"/><path d="M14 3a7 7 0 0 1 7 7M14 6.5a3.5 3.5 0 0 1 3.5 3.5" stroke="#c41e27" stroke-width="1.8" fill="none"/></svg>
      <span class="contact__text">07 842 1937</span>
    </li>
    <li class="contact">
      <svg class="contact__icon" viewBox="0 0 24 24" aria-hidden="true"><rect x="5.5" y="2" width="13" height="20" rx="2" fill="none" stroke="#c41e27" stroke-width="2"/><circle cx="12" cy="18.5" r="1" fill="#c41e27"/></svg>
      <span class="contact__text">027 519 2764</span>
    </li>
    <li class="contact">
      <svg class="contact__icon" viewBox="0 0 24 24" aria-hidden="true"><rect x="1" y="5" width="22" height="14" fill="#c41e27"/><path d="M1 5l11 8 11-8" stroke="#000" stroke-width="1.5" fill="none"/></svg>
      <span class="contact__text contact__text--small">office@ridgebackmotors.co.nz</span>
    </li>
    <li class="contact contact--web">
      <svg class="contact__icon" viewBox="0 0 24 24" aria-hidden="true"><g fill="none" stroke="#c41e27" stroke-width="1.5"><circle cx="11" cy="11" r="9.5"/><ellipse cx="11" cy="11" rx="4" ry="9.5"/><path d="M1.5 11h19M3 6h16M3 16h16"/></g><path d="M14 14l8 3-3.5 1.2L17 22z" fill="#c41e27"/></svg>
      <span class="contact__text contact__text--small">ridgebackmotors.co.nz</span>
    </li>
  </ul>
</section>

<section class="card card--back" aria-label="Business card back">
  <div class="brand-name">Ridgeback Prime Automotive</div>

  <div class="appointment">
    <h2 class="appointment__title">Appointment details</h2>
    <div class="field"><span>Date:</span><span class="field__line"></span></div>
    <div class="field"><span>Time:</span><span class="field__line"></span></div>
  </div>

  <div class="services">
    <ul class="services__group"><li>Vehicle Servicing</li><li>Tyres &amp; Wheel Alignments</li></ul>
    <ul class="services__group"><li>All Mechanical Repairs</li><li>Automotive Diagnostic</li></ul>
    <ul class="services__group"><li>Warrant of Fitness</li><li>Automotive Parts &amp; Supplies</li></ul>
  </div>
</section>

</body>
</html>
```